Cutting Edge Ultra High End Investment Company & Business Card

We are an Ultra High End PRIVATE Investment Group that is known for being ULTRA EXCLUSIVE and High NET WORTH. We are kind of the Meridian Vault Onyx for the private investment space in Orange County California, we only invite new investors by referral only.
We are looking for a information only web site that has a big impact once we invite new investors to our site. It needs to be Ultra Modern, Sophisticated, and make an impact. The only contact information that will be listed on the web site is a place where if invite a new investor they can enter a code to unlock access to our members contacts (future page)
We are like the look of a full size web lay out where it has a very large full screen image background.
We are open to any fonts any colors and any designs.
Target Market(s)
Private investors for information only
Industry/Entity Type
Business
Contact Information for Business Card
Please see attached jpeg. this is a very GENERIC
Number of Pages Required
1 page
Requirements
Must have
- Modern, Cutting Edge, Big Impact
Nice to have
- All the info that currently on VR Business Card Attached
Should not have
- Boxing gloves

```html
<!DOCTYPE html>
<html lang="en">
<head>
<meta charset="utf-8">
<title>VR Investment Group</title>
<link rel="stylesheet" href="https://fonts.googleapis.com/css2?family=Open+Sans:wght@300;400;600;700&family=Raleway:wght@400;600&display=swap">
<style>
:root{
  --ink:#333a40;
  --muted:#7b8288;
  --accent:#1f6f96;
  --light:#f1f1f1;
  --footer:#2b2b2b;
  --footer-deep:#1f1f1f;
  --footer-text:#a8a8a8;
  --white:#ffffff;
}
*{box-sizing:border-box;margin:0;padding:0}
html,body{width:739px;height:1200px;overflow:hidden}
body{font-family:"Open Sans",Arial,sans-serif;color:var(--ink);background:var(--white);font-size:7px;line-height:1.5}
.site-header{height:40px;display:flex;align-items:center;justify-content:space-between;padding:0 58px 0 60px;background:var(--white)}
.brand{display:flex;align-items:center;gap:6px;font-weight:700;font-size:11px;letter-spacing:.5px;color:var(--ink);line-height:1.1}
.brand-mark{width:14px;height:14px;background:var(--ink)}
.brand small{font-size:5.5px;font-weight:600;letter-spacing:.6px;display:block}
.main-nav{display:flex;gap:30px;font-size:6.5px;color:var(--ink)}
.hero{height:270px;background:linear-gradient(180deg,#3c3b45 0%,#8c5a3a 30%,#d98a3b 48%,#6e4a38 62%,#2b3440 100%);display:flex;flex-direction:column;align-items:center;justify-content:center;color:var(--white);text-align:center}
.hero h1{font-weight:700;font-size:30px;letter-spacing:1px;line-height:1.1}
.hero p{font-family:"Raleway",sans-serif;font-size:15px;letter-spacing:.5px;margin-top:2px}
.btn{display:inline-block;font-size:6px;font-weight:700;letter-spacing:.6px;text-transform:uppercase;color:var(--white);padding:7px 16px;border-radius:12px}
.hero .btn{background:rgba(20,20,20,.75);margin-top:14px}
.section-title{font-family:"Raleway",sans-serif;font-size:13px;font-weight:600;text-align:center;color:var(--ink)}
.section-intro{text-align:center;color:var(--muted);width:470px;margin:8px auto 0;font-size:6.5px}
.welcome{height:195px;padding-top:26px}
.sectors{display:flex;gap:26px;width:630px;margin:24px auto 0}
.sector{flex:1}
.sector h3{display:flex;align-items:center;gap:6px;font-size:8px;font-weight:600;margin-bottom:6px}
.sector svg{width:14px;height:14px;stroke:var(--ink);fill:none;stroke-width:1.5}
.sector p{color:var(--muted);font-size:6px;padding-left:20px}
.about{height:210px;background:var(--light);display:flex;gap:32px;padding:28px 52px 0 62px}
.about-photo{width:226px;height:155px;flex:none;background:linear-gradient(135deg,#c9cfd6,#8d98a4 60%,#5b6470)}
.about-copy{flex:1}
.about-copy h2{font-family:"Raleway",sans-serif;font-size:12px;font-weight:600;margin-bottom:8px}
.about-copy p{color:var(--muted);font-size:6px;margin-bottom:8px}
.about-copy .btn{background:var(--accent);margin-top:4px}
.news{height:270px;padding-top:24px}
.news-grid{display:flex;gap:14px;width:615px;margin:20px auto 0}
.news-item{flex:1}
.news-photo{height:85px}
.p1{background:linear-gradient(135deg,#e7e9ec,#b7bdc4)}
.p2{background:linear-gradient(135deg,#6e6a66,#2e2c2b)}
.p3{background:linear-gradient(135deg,#d9dcdf,#8f959c)}
.p4{background:linear-gradient(135deg,#7d8b99,#2f3a46)}
.news-item h4{font-size:7px;font-weight:600;margin-top:6px}
.news-item time{font-size:5.5px;color:var(--muted)}
.site-footer{height:191px;background:var(--footer);color:var(--footer-text);display:grid;grid-template-columns:210px 110px 120px 1fr;gap:28px;padding:24px 52px 0 62px}
.site-footer h5{color:var(--white);font-size:7px;font-weight:700;letter-spacing:.5px;text-transform:uppercase;padding-bottom:6px;border-bottom:1px solid #444;margin-bottom:10px}
.site-footer li{list-style:none;font-size:6px;margin-bottom:5px}
.quote{font-size:6px;font-style:italic;position:relative;padding-left:12px}
.quote:before{content:"\201C";position:absolute;left:0;top:-4px;font-size:14px;color:var(--white)}
.author{display:flex;align-items:center;gap:8px;margin-top:14px;padding-left:12px}
.author span{width:22px;height:22px;border-radius:50%;background:#6b6b6b}
.author b{color:var(--white);font-size:6px;display:block}
.author em{font-size:5px;font-style:normal}
.col-social li{display:flex;align-items:center;gap:7px;margin-bottom:8px}
.col-social li span{width:13px;height:13px;border-radius:50%;background:#4a4a4a}
.copyright{height:24px;background:var(--footer-deep);color:#888;font-size:5.5px;text-align:center;line-height:24px}
</style>
</head>
<body>
<header class="site-header">
  <div class="brand"><span class="brand-mark"></span><div>VR<small>INVESTMENT GROUP</small></div></div>
  <nav class="main-nav"><span>Home</span><span>About Us</span><span>Services</span><span>News</span><span>Testimonials</span><span>Contact Us</span></nav>
</header>

<section class="hero" role="img" aria-label="Sunset over the ocean beside a long pier">
  <h1>VR INVESTMENT GROUP</h1>
  <p>WE ARE A ULTRA HIGH END INVESTMENT COMPANY GROUP</p>
  <span class="btn">View our history</span>
</section>

<section class="welcome">
  <h2 class="section-title">Welcome to VR Investments</h2>
  <p class="section-intro">VR Investments is the privately held investment and holding company located in Crestline Bay, Westmora. We only accept new investors by referral or invitation only.</p>
  <div class="sectors">
    <div class="sector"><h3><svg viewBox="0 0 14 14"><path d="M2 7 7 2.5 12 7M3.5 6v6h7V6"/></svg>Residential</h3><p>Select coastal homes held for long term value and steady growth.</p></div>
    <div class="sector"><h3><svg viewBox="0 0 14 14"><rect x="3" y="2" width="8" height="10"/><path d="M5 5h1M8 5h1M5 8h1M8 8h1"/></svg>Commercial</h3><p>Office and mixed use property placed in prime business districts.</p></div>
    <div class="sector"><h3><svg viewBox="0 0 14 14"><path d="M3 5h8l-1 7H4z"/><path d="M5 5a2 2 0 0 1 4 0"/></svg>Retail</h3><p>Premium storefronts in centers with strong and loyal foot traffic.</p></div>
    <div class="sector"><h3><svg viewBox="0 0 14 14"><path d="M3 8a4 4 0 0 1 8 0"/><rect x="2" y="8" width="2" height="3"/><rect x="10" y="8" width="2" height="3"/></svg>Telecommunications</h3><p>Network assets and tower sites that earn reliable yearly income.</p></div>
  </div>
</section>

<section class="about">
  <div class="about-photo" role="img" aria-label="Business team seated at a meeting table"></div>
  <div class="about-copy">
    <h2>About VR Investments</h2>
    <p>VR Investments is the privately held investment and holding company located in Crestline Bay, Westmora. We only accept new investors by referral or invitation. Since our founding we have served a small circle of partners with patient capital and discreet, careful guidance across every holding.</p>
    <p>We are a diversified investment group composed of high net worth private investors actively investing in residential, commercial, retail, and telecommunications assets as well as select private ventures.</p>
    <span class="btn">Read more info</span>
  </div>
</section>

<section class="news">
  <h2 class="section-title">Latest News</h2>
  <p class="section-intro">VR Investments is the privately held investment and holding company located in Crestline Bay, Westmora. We only accept new investors by referral only.</p>
  <div class="news-grid">
    <article class="news-item"><div class="news-photo p1" role="img" aria-label="Hands reviewing documents on a desk"></div><h4>Quarterly review for our partners</h4><time>Posted on 27 march 2015</time></article>
    <article class="news-item"><div class="news-photo p2" role="img" aria-label="Two people shaking hands"></div><h4>New holding added to portfolio</h4><time>Posted on 27 march 2015</time></article>
    <article class="news-item"><div class="news-photo p3" role="img" aria-label="Colleagues working together at a table"></div><h4>Coastal property market update</h4><time>Posted on 27 march 2015</time></article>
    <article class="news-item"><div class="news-photo p4" role="img" aria-label="Businessman working on a laptop"></div><h4>Annual members gathering news</h4><time>Posted on 27 march 2015</time></article>
  </div>
</section>

<footer class="site-footer">
  <div class="col-testimonial">
    <h5>Testimonials</h5>
    <p class="quote">Working with this group has been a rare privilege. Their patience, discretion and steady judgement have grown our family holdings year after year with real care.</p>
    <div class="author"><span></span><div><b>DANIEL HARLOW</b><em>Private Investor</em></div></div>
  </div>
  <div class="col-links">
    <h5>Welcome</h5>
    <ul><li>Home</li><li>About Us</li><li>Services</li><li>News</li><li>Testimonials</li><li>Contact Us</li></ul>
  </div>
  <div class="col-links">
    <h5>Information</h5>
    <ul><li>Privacy Policy</li><li>Terms &amp; Conditions</li><li>Site Map</li></ul>
  </div>
  <div class="col-social">
    <h5>Follow Us</h5>
    <ul><li><span></span>Feedline</li><li><span></span>Chirpnet</li><li><span></span>Linkwork</li><li><span></span>Circlespace</li></ul>
  </div>
</footer>
<div class="copyright">© 2015 VR Investment Group. All Rights Reserved.</div>
</body>
</html>
```